Yoga Studio Postcard Advertising Flyer

Need a postcard size flyer that will promote our business. The objective is to promote location and availability. Want it to be personal. The objective to connect the audience to the purpose of yoga and the focus on enabling functional well-being. Something that is a very big focus at this point in time in the world. I really want people to see the value in connecting with us via our website, calmora app, pagewell or vibro. The colours are to be bright but not overwhelming and aligned to the logo colours. Its also important to have the location picture on the flyer - unless you think that it is way too much (try a with or without). I don't want this to be a specials brochure - it is an introduction to our brand and our business. No need to over do it with promotional lines apart from come and join us.

Delayed in organising this.

Local yogis and residence who are or want to be focused on well-being.

• Pictures - would have the logo on one side.
• Modern and aligned to website design.

```html
<!DOCTYPE html>
<html lang="en">
<head>
<meta charset="utf-8">
<title>Crane Petal Yoga – Postcard</title>
<link rel="stylesheet" href="https://fonts.googleapis.com/css2?family=Archivo+Black&family=Roboto:wght@300;400;700;900&display=swap">
<style>
  :root {
    --sky: #1fa2db;
    --navy: #101a3a;
    --ink: #111111;
    --white: #ffffff;
    --page: #f4f5f7;
  }
  * { margin: 0; padding: 0; box-sizing: border-box; }
  html, body { width: 1200px; height: 849px; overflow: hidden; background: var(--page); }
  .postcard {
    position: absolute; left: 0; top: 62px; width: 1200px; height: 726px;
    background: var(--white); overflow: hidden;
    font-family: "Roboto", Arial, sans-serif;
  }
  .band { position: absolute; left: 0; width: 100%; }
  .band--top { top: 0; height: 76px; background: var(--sky); }
  .band--tagline { top: 300px; height: 50px; background: var(--sky); }
  .band--contact { top: 602px; height: 70px; background: var(--navy); }
  .band--address { top: 684px; height: 42px; background: var(--navy); }

  .invite {
    position: absolute; left: 28px; top: 14px;
    font-family: "Roboto", Arial, sans-serif; font-weight: 900;
    font-size: 42px; color: var(--white); letter-spacing: 0.3px;
  }
  .brand-name {
    position: absolute; left: 36px; top: 186px; width: 210px;
    text-align: center; color: var(--navy);
    font-weight: 400; font-size: 29px; line-height: 34px; letter-spacing: 1px;
  }
  .brand-dot {
    position: absolute; left: 111px; top: 112px; width: 60px; height: 60px;
    border-radius: 50%; background: var(--sky);
  }
  .headline {
    position: absolute; left: 266px; top: 112px;
    font-family: "Archivo Black", "Arial Black", sans-serif;
    font-size: 52px; line-height: 48px; color: var(--sky); letter-spacing: 1px;
  }
  .tagline {
    position: absolute; right: 516px; top: 312px;
    font-weight: 900; font-size: 17px; color: var(--white); letter-spacing: 0.2px;
  }
  .intro {
    position: absolute; right: 516px; top: 383px; width: 680px;
    text-align: right; font-size: 21px; line-height: 26px; color: var(--ink);
    letter-spacing: -0.2px;
  }
  .vision {
    position: absolute; left: 323px; top: 506px;
    font-weight: 300; font-size: 22px; line-height: 26px; color: var(--sky);
    letter-spacing: 0.6px;
  }
  .photo { position: absolute; }
  .photo--studio { left: 676px; top: 27px; }
  .photo--building { left: 12px; top: 457px; }
  .photo--teacher { left: 920px; top: 432px; }

  .contact { position: absolute; top: 602px; height: 70px; display: flex; align-items: center; color: var(--white); }
  .contact--web { left: 270px; gap: 12px; font-weight: 700; font-size: 21px; letter-spacing: 0.5px; }
  .contact--social { left: 612px; gap: 26px; font-size: 19px; font-weight: 400; }
  .social { display: flex; align-items: center; gap: 7px; }
  .social-dot { width: 12px; height: 12px; border-radius: 50%; background: var(--sky); }
  .address {
    position: absolute; left: 275px; top: 684px; height: 42px;
    display: flex; align-items: center; gap: 10px;
    color: var(--white); font-size: 20px; letter-spacing: 0.4px;
  }
</style>
</head>
<body>
<main class="postcard">
  <div class="band band--top"></div>
  <div class="band band--tagline"></div>
  <div class="band band--contact"></div>
  <div class="band band--address"></div>

  <h2 class="invite">Come join us!</h2>

  <div class="brand-dot"></div>
  <div class="brand-name">CRANE PETAL<br>YOGA</div>

  <h1 class="headline">ENABLE<br>FUNCTIONAL<br>WELLBEING</h1>

  <p class="tagline">STRENGTHEN YOUR WELL-BEING THROUGH ADAPTIVE YOGA.</p>

  <p class="intro">Seek to evolve your mind and body through the challenge of yoga.<br>Perfection is a desire and never an outcome through the<br>practice of yoga.</p>

  <p class="vision">Our vision is to create an atmosphere that<br>enables inclusiveness of the whole community.</p>

  <svg class="photo photo--studio" width="508" height="452" viewBox="0 0 508 452" role="img" aria-label="Photo of the sunlit studio room with wooden floor and rows of blue yoga mats">
    <defs>
      <linearGradient id="studioTone" x1="0" y1="0" x2="0" y2="1">
        <stop offset="0" stop-color="#dcd6cf"/>
        <stop offset="0.45" stop-color="#c9c0b6"/>
        <stop offset="0.6" stop-color="#8a4a26"/>
        <stop offset="1" stop-color="#5b2c14"/>
      </linearGradient>
    </defs>
    <polygon points="128,12 380,12 496,226 380,440 128,440 12,226" fill="url(#studioTone)" stroke="url(#studioTone)" stroke-width="24" stroke-linejoin="round"/>
  </svg>

  <svg class="photo photo--building" width="266" height="242" viewBox="0 0 266 242" role="img" aria-label="Photo of the chapel building exterior with picket fence">
    <defs>
      <linearGradient id="buildingTone" x1="0" y1="0" x2="0" y2="1">
        <stop offset="0" stop-color="#8fa3bd"/>
        <stop offset="0.45" stop-color="#c9c8c4"/>
        <stop offset="1" stop-color="#7b6a5c"/>
      </linearGradient>
    </defs>
    <polygon points="70,10 196,10 254,121 196,232 70,232 12,121" fill="url(#buildingTone)" stroke="url(#buildingTone)" stroke-width="20" stroke-linejoin="round"/>
  </svg>

  <svg class="photo photo--teacher" width="248" height="230" viewBox="0 0 248 230" role="img" aria-label="Black and white portrait photo of the yoga teacher">
    <defs>
      <linearGradient id="teacherTone" x1="0" y1="0" x2="0" y2="1">
        <stop offset="0" stop-color="#d8d8d8"/>
        <stop offset="0.6" stop-color="#9a9a9a"/>
        <stop offset="1" stop-color="#e4e4e4"/>
      </linearGradient>
    </defs>
    <polygon points="64,10 184,10 238,115 184,220 64,220 10,115" fill="url(#teacherTone)" stroke="url(#teacherTone)" stroke-width="20" stroke-linejoin="round"/>
  </svg>

  <div class="contact contact--web">
    <svg width="42" height="42" viewBox="0 0 42 42" aria-hidden="true">
      <g fill="none" stroke="#ffffff" stroke-width="2.4">
        <circle cx="21" cy="21" r="19"/>
        <ellipse cx="21" cy="21" rx="8" ry="19"/>
        <line x1="21" y1="2" x2="21" y2="40"/>
        <line x1="2" y1="21" x2="40" y2="21"/>
        <path d="M5 12 H37 M5 30 H37"/>
      </g>
    </svg>
    <span>cranepetalyoga.com.au</span>
  </div>

  <div class="contact contact--social">
    <span class="social"><span class="social-dot"></span>pagewell</span>
    <span class="social"><span class="social-dot"></span>vibro</span>
    <span class="social"><span class="social-dot"></span>calmora</span>
  </div>

  <div class="address">
    <svg width="20" height="30" viewBox="0 0 20 30" aria-hidden="true">
      <path d="M10 28 C4 19 2 15 2 10 A8 8 0 0 1 18 10 C18 15 16 19 10 28 Z" fill="none" stroke="#ffffff" stroke-width="2.2"/>
      <circle cx="10" cy="10" r="3" fill="#ffffff"/>
    </svg>
    <span>The Chapel, 214 Harbour Lane Seaview NSW 2099</span>
  </div>
</main>
</body>
</html>
```